Business Cards - Brightway Harbor

need to design unique business card for my mortgage business. I need to design credit card style business card for my business or any unique idea that you might have

Target Market(s)

Home Loan customers

Industry/Entity Type

Mortgage Brokerage

Contact Information for Business Card

please design credit card style or very unique style business card

Colors

Designer to choose colors to be used in the design.

Requirements
Must have
• Name
• position
• Phone number
• fax number
• email address
• website address
• social media address
• All above fields will be provided once design in finalised

```html
<!DOCTYPE html>
<html lang="en">
<head>
<meta charset="utf-8">
<title>Brightway Harbor — Business Card</title>
<link rel="stylesheet" href="https://fonts.googleapis.com/css2?family=Work+Sans:wght@400;500&family=Tinos&display=swap">
<style>
  :root {
    --page-bg: #e6e1da;
    --card-bg: #f4eee6;
    --navy: #2f3b73;
    --orange: #d9812f;
    --text-grey: #5a5a5e;
    --decor: #c9b8a0;
  }
  * { margin: 0; padding: 0; box-sizing: border-box; }
  html, body {
    width: 1200px;
    height: 1047px;
    overflow: hidden;
    background: var(--page-bg);
  }
  .card {
    position: absolute;
    left: 100px;
    top: 252px;
    width: 1000px;
    height: 543px;
    border-radius: 20px;
    background: var(--card-bg);
    overflow: hidden;
    box-shadow: 0 10px 30px rgba(60, 45, 30, 0.12);
    font-family: "Work Sans", Arial, sans-serif;
  }
  .tree-decoration {
    position: absolute;
    left: 434px;
    top: 12px;
    width: 560px;
    height: 456px;
    border-radius: 50% 50% 40% 40%;
    background: radial-gradient(ellipse at 50% 40%, rgba(201,184,160,0.45) 0%, rgba(201,184,160,0.2) 55%, rgba(201,184,160,0) 75%);
  }
  .brand {
    position: absolute;
    left: 57px;
    top: 118px;
    display: flex;
    align-items: center;
    gap: 14px;
  }
  .brand-mark {
    width: 18px;
    height: 18px;
    background: var(--orange);
  }
  .brand-name {
    font-weight: 500;
    font-size: 40px;
    color: var(--navy);
    letter-spacing: 0.5px;
  }
  .person {
    position: absolute;
    right: 48px;
    top: 248px;
    text-align: right;
  }
  .person-name {
    font-family: "Tinos", "Times New Roman", serif;
    font-size: 37px;
    color: var(--navy);
    line-height: 1;
    letter-spacing: 0.3px;
  }
  .person-role {
    margin-top: 12px;
    font-size: 21px;
    color: var(--orange);
    letter-spacing: 0.6px;
    line-height: 1;
  }
  .divider {
    position: absolute;
    left: 51px;
    top: 321px;
    width: 903px;
    height: 2px;
    background: var(--navy);
  }
  .address {
    position: absolute;
    left: 51px;
    top: 352px;
    font-size: 22px;
    line-height: 28px;
    color: var(--text-grey);
    font-style: normal;
  }
  .contacts {
    position: absolute;
    left: 51px;
    top: 420px;
    list-style: none;
    font-size: 22px;
    line-height: 28.5px;
    color: var(--text-grey);
  }
  .contacts li {
    display: flex;
    align-items: center;
    gap: 14px;
  }
  .contacts svg {
    width: 14px;
    height: 14px;
    flex: none;
  }
  .swoosh {
    position: absolute;
    left: 0;
    top: 0;
    width: 1000px;
    height: 543px;
  }
</style>
</head>
<body>
  <section class="card">
    <div class="tree-decoration" role="img" aria-label="Faint tree illustration in warm beige tones"></div>

    <div class="brand">
      <span class="brand-mark"></span>
      <span class="brand-name">Brightway Harbor</span>
    </div>

    <div class="person">
      <div class="person-name">DANIEL HARTLEY</div>
      <div class="person-role">Founder</div>
    </div>

    <div class="divider"></div>

    <address class="address">
      2480 Seabreeze Ave.<br>
      Coral Point, FL 33012
    </address>

    <ul class="contacts">
      <li>
        <svg viewBox="0 0 14 14" aria-hidden="true"><path d="M3 1.5 L5 1.5 L6 4.5 L4.6 5.6 Q5.8 8.2 8.4 9.4 L9.5 8 L12.5 9 L12.5 11 Q12.5 12.5 11 12.5 Q2 12 1.5 3 Q1.5 1.5 3 1.5 Z" fill="var(--orange)"/></svg>
        555-318-4072
      </li>
      <li>
        <svg viewBox="0 0 14 14" aria-hidden="true"><rect x="1.5" y="3" width="11" height="8" fill="none" stroke="var(--orange)" stroke-width="1.4"/><path d="M1.5 3 L7 7.5 L12.5 3" fill="none" stroke="var(--orange)" stroke-width="1.4"/></svg>
        hello@brightwayharbor.com
      </li>
      <li>
        <svg viewBox="0 0 14 14" aria-hidden="true"><circle cx="7" cy="7" r="5.5" fill="var(--orange)"/></svg>
        www.BrightwayHarbor.com
      </li>
    </ul>

    <svg class="swoosh" viewBox="0 0 1000 543" aria-hidden="true">
      <path d="M445 543 Q700 470 1000 461 L1000 543 Z" fill="var(--orange)"/>
      <path d="M512 543 Q760 478 1000 469 L1000 543 Z" fill="var(--navy)"/>
    </svg>
  </section>
</body>
</html>
```